Brochure Design Project

Trifold A4 brochure stating what we do:
Picture Framer
Fine Art Printing
Digital Press Printing
Photographer
Gallery
Studio
We have full time experienced framer
2 x Calvor 4400 large format printers
Tarno Plexa K52 Digital press printer 1st one in State of Tasmania
Will print business cards, brochures, books, postcards, etc more info available on Tarno Plexa website.
Photography: Studio, Art reproduction, Wedding, Portrait,Commercial, etc.
Gallery & studio for hire

Website www.wendlequaypress.com

The Tarno Plexa K52 printer is new addition to business. There should be more on going business for customers wanting graphic design done for printing jobs.

```html
<!DOCTYPE html>
<html lang="en">
<head>
<meta charset="utf-8">
<title>Wendle Quay Press – Trifold Brochure</title>
<link rel="stylesheet" href="https://fonts.googleapis.com/css2?family=Open+Sans:wght@400;600;700&family=Oswald:wght@500;600&display=swap">
<style>
:root{
  --magenta:#e5007d;
  --cyan:#1ba3e0;
  --orange:#f7941d;
  --green:#3aaa35;
  --blue:#2c4f9e;
  --ink:#231f20;
  --panel-dark:#1c1a1b;
  --paper:#ffffff;
  --stage:#e8e5e1;
  --body-grey:#3a3a3a;
}
*{box-sizing:border-box;margin:0;padding:0}
html,body{width:1048px;height:1200px;overflow:hidden}
body{background:var(--stage);font-family:"Open Sans",Arial,sans-serif;position:relative}
.sheet{position:absolute;left:136px;width:775px;height:548px;display:flex;box-shadow:0 4px 14px rgba(0,0,0,.25);overflow:hidden}
.sheet--front{top:40px}
.sheet--inside{top:612px}
.panel{position:relative;width:258.33px;height:100%;overflow:hidden}
.panel--dark{background:var(--ink);color:#fff}
.panel--white{background:var(--paper);color:var(--body-grey)}
.photo{position:absolute}
.stripes{position:absolute;left:0;top:0;pointer-events:none}
.services{position:absolute;font-family:"Oswald","Arial Narrow",sans-serif;font-weight:600;font-size:13.5px;line-height:17px;letter-spacing:.2px;color:#fff}
.services li{list-style:none;position:relative}
.logo-disc{position:absolute;border-radius:50%;background:#fff;display:flex;align-items:center;justify-content:center;text-align:center}
.logo-name{font-family:"Open Sans",Arial,sans-serif;font-weight:600;color:var(--magenta);line-height:1.05}

/* front panel 1 */
.about-box{position:absolute;left:20px;top:50px;width:238px;height:388px;background:#0d0c0c;border-radius:14px 0 0 14px}
.about-badge{position:absolute;left:34px;top:35px;width:80px;height:46px}
.about-badge span{position:absolute;border-radius:50%;width:46px;height:46px}
.about-badge .dot-a{left:0;background:var(--magenta)}
.about-badge .dot-b{left:28px;background:var(--orange)}
.about-badge b{position:absolute;left:7px;top:13px;font-weight:400;font-size:14px;color:#fff;white-space:nowrap}
.about-copy{position:absolute;left:34px;top:113px;width:206px;font-size:8.4px;line-height:11px;color:#eee}
.about-copy p+p{margin-top:10px}
.call-us{position:absolute;left:88px;top:392px;width:112px;height:112px;border-radius:50%;background:var(--cyan);color:#fff;text-align:center;padding-top:36px}
.call-us strong{display:block;font-weight:400;font-size:17px;line-height:18px}
.call-us span{font-size:12px}

/* front panel 2 */
.press-claim{position:absolute;left:0;width:100%;top:272px;text-align:center;font-weight:700;font-size:11.5px;line-height:16px;color:var(--ink)}
.badge-plain{position:absolute;left:88px;top:332px;width:82px;height:82px;border-radius:50%;background:#fff;border:3px solid var(--ink);box-shadow:0 0 0 2px #fff,0 0 0 3px #999}
.contact{position:absolute;left:0;width:100%;top:440px;text-align:center;font-size:7.4px;line-height:9px;font-weight:700;color:var(--ink)}
.contact .gap{margin-top:6px}
.contact .web{font-size:9px;line-height:11px;font-weight:400;margin-top:5px}

/* inside panel 1 */
.inside-claim{position:absolute;left:0;width:100%;top:272px;text-align:center;font-weight:700;font-size:11.5px;line-height:16px;color:var(--orange)}
.printers{position:absolute;left:0;width:100%;top:314px;text-align:center;font-weight:700;font-size:12px}
.printers-note{position:absolute;left:22px;width:214px;top:330px;text-align:center;font-size:8px;line-height:10.5px}
.photo-services{position:absolute;left:22px;width:214px;top:360px;text-align:center;font-weight:700;font-size:9px;line-height:13px;color:var(--cyan)}
.photo-services em{font-style:normal;font-size:12.5px}
.services--centred{left:0;width:100%;top:458px;text-align:center;font-size:13.5px}

/* inside panel 2 */
.market-title{position:absolute;left:17px;top:112px;font-size:10px;color:var(--magenta)}
.market-copy{position:absolute;left:17px;width:215px;top:130px;font-size:8.4px;line-height:11px;color:var(--body-grey)}
.market-copy p+p{margin-top:10px}
.names{color:var(--orange)}

/* inside panel 3 */
.profile-box{position:absolute;left:20px;top:254px;width:238.33px;height:294px;background:#0d0c0c;color:#fff;border-radius:14px 0 0 0;padding:20px 14px 0 14px}
.profile-box h2{font-size:12px;font-weight:700;color:#fff}
.profile-box .where{font-size:8.5px;color:var(--magenta);margin-top:1px}
.profile-box p{font-size:8.4px;line-height:11px;margin-top:11px;color:#eee}
.profile-box p.names{color:var(--orange)}
.profile-box .web{position:absolute;left:14px;bottom:14px;font-size:9.5px;font-weight:700;letter-spacing:.4px;color:#fff}
</style>
</head>
<body>

<!-- FRONT -->
<section class="sheet sheet--front" aria-label="Brochure front">
  <div class="panel" aria-label="About us panel">
    <div class="photo" role="img" aria-label="Colourful graffiti laneway photograph" style="inset:0;background:linear-gradient(160deg,#6d4f8a 0%,#8e6e95 30%,#a49aa0 60%,#7d7570 100%)"></div>
    <div class="about-box"></div>
    <div class="about-badge"><span class="dot-a"></span><span class="dot-b"></span><b>About Us</b></div>
    <div class="about-copy">
      <p>Ned Arlow has had a long passion for photography. He decided to take photography seriously in 2008 by studying full time at Polytechnic to obtain his Diploma in Photo Imaging. At the same time he rented a studio at 48 Corrin Street Wendle. The business has now moved to larger premises at 112 Baylis Street.</p>
      <p>Ned's camera equipment includes the Orrin 5X Mark III, 1x Mark III and also the Orrin 7X He has a number of quality lenses and accessories. There is also a fully equipped studio, which is available for hire.</p>
      <p>Apart from landscape photography Ned has experience with portrait, commercial, wedding and real estate photography.<br>Fine art printing is done on the large format Calvor 4400 printer. It uses Lumachrome K3 inks, which gives lightfastness ratings for up to 75 years for colour and over 200 years for black and white.</p>
    </div>
    <div class="call-us"><strong>CALL US</strong><span>03 6100 2741</span></div>
  </div>

  <div class="panel panel--white" aria-label="Contact panel">
    <svg class="photo" width="258" height="270" viewBox="0 0 258 270" role="img" aria-label="Styled photograph of two women seated in a sunny park">
      <defs><linearGradient id="parkTone" x1="0" y1="0" x2="0" y2="1"><stop offset="0" stop-color="#d9c9a8"/><stop offset=".55" stop-color="#a08a6a"/><stop offset="1" stop-color="#5f6b3a"/></linearGradient></defs>
      <path d="M0 0H232C272 90 210 220 0 252Z" fill="url(#parkTone)"/>
      <path d="M232 0C272 90 210 220 0 252" fill="none" stroke="var(--magenta)" stroke-width="7"/>
    </svg>
    <p class="press-claim">Tarno Plexa K52 Digital press printer<br>1st one in State of Tasmania</p>
    <div class="badge-plain" role="img" aria-label="Accreditation badge"></div>
    <div class="contact">
      <div>WENDLE QUAY PRESS</div>
      <div>112 Baylis Street</div>
      <div>Wendle, Tasmania 7010</div>
      <div class="gap">P: 03 6100 2741</div>
      <div>M: 0400 118 552</div>
      <div class="gap">Email: ned@wendlequaypress.com</div>
      <div class="web">www.wendlequaypress.com</div>
    </div>
  </div>

  <div class="panel panel--dark" aria-label="Cover panel">
    <ul class="services" style="left:30px;top:20px">
      <li>Picture Framer</li><li>Fine Art Printing</li><li>Digital Press Printing</li><li>Photographer</li><li>Gallery Studio</li>
    </ul>
    <svg class="stripes" width="258" height="548" viewBox="0 0 258 548" aria-hidden="true">
      <g stroke-width="6">
        <line x1="0" y1="27" x2="24" y2="27" stroke="var(--magenta)"/>
        <line x1="0" y1="44" x2="24" y2="44" stroke="var(--cyan)"/>
        <line x1="0" y1="61" x2="24" y2="61" stroke="var(--orange)"/>
        <line x1="0" y1="78" x2="24" y2="78" stroke="var(--green)"/>
        <line x1="0" y1="95" x2="24" y2="95" stroke="var(--blue)"/>
      </g>
    </svg>
    <div class="photo" role="img" aria-label="Circular photograph of a graffiti covered laneway" style="left:12px;top:146px;width:234px;height:234px;border-radius:50%;background:radial-gradient(circle at 40% 45%,#d35aa0 0%,#7b5ab0 35%,#3d6aa8 65%,#5a8c5a 100%)"></div>
    <svg class="stripes" width="258" height="548" viewBox="0 0 258 548" aria-hidden="true">
      <g stroke-width="6">
        <line x1="0" y1="445" x2="110" y2="445" stroke="var(--magenta)"/>
        <line x1="0" y1="460" x2="110" y2="460" stroke="var(--cyan)"/>
        <line x1="0" y1="475" x2="110" y2="475" stroke="var(--orange)"/>
        <line x1="0" y1="490" x2="110" y2="490" stroke="var(--green)"/>
        <line x1="0" y1="505" x2="110" y2="505" stroke="var(--blue)"/>
      </g>
      <g stroke-width="6">
        <line x1="133" y1="520" x2="133" y2="548" stroke="var(--magenta)"/>
        <line x1="149" y1="520" x2="149" y2="548" stroke="var(--cyan)"/>
        <line x1="165" y1="520" x2="165" y2="548" stroke="var(--orange)"/>
        <line x1="181" y1="520" x2="181" y2="548" stroke="var(--green)"/>
        <line x1="197" y1="520" x2="197" y2="548" stroke="var(--blue)"/>
      </g>
    </svg>
    <div class="logo-disc" style="left:95px;top:378px;width:152px;height:152px">
      <span class="logo-name" style="font-size:21px">Wendle<br>Quay</span>
    </div>
  </div>

  <svg class="stripes" width="775" height="548" viewBox="0 0 775 548" aria-hidden="true">
    <g stroke-width="6">
      <line x1="258" y1="445" x2="304" y2="445" stroke="var(--magenta)"/><line x1="455" y1="445" x2="516" y2="445" stroke="var(--magenta)"/>
      <line x1="258" y1="460" x2="304" y2="460" stroke="var(--cyan)"/><line x1="455" y1="460" x2="516" y2="460" stroke="var(--cyan)"/>
      <line x1="258" y1="475" x2="304" y2="475" stroke="var(--orange)"/><line x1="455" y1="475" x2="516" y2="475" stroke="var(--orange)"/>
      <line x1="258" y1="490" x2="304" y2="490" stroke="var(--green)"/><line x1="455" y1="490" x2="516" y2="490" stroke="var(--green)"/>
      <line x1="258" y1="505" x2="304" y2="505" stroke="var(--blue)"/><line x1="455" y1="505" x2="516" y2="505" stroke="var(--blue)"/>
    </g>
  </svg>
</section>

<!-- INSIDE -->
<section class="sheet sheet--inside" aria-label="Brochure inside">
  <div class="panel panel--dark" aria-label="Services panel">
    <svg class="stripes" width="258" height="548" viewBox="0 0 258 548" aria-hidden="true">
      <g stroke-width="6">
        <line x1="0" y1="22" x2="258" y2="22" stroke="var(--magenta)"/>
        <line x1="0" y1="38" x2="258" y2="38" stroke="var(--cyan)"/>
        <line x1="0" y1="54" x2="258" y2="54" stroke="var(--orange)"/>
        <line x1="0" y1="70" x2="258" y2="70" stroke="var(--green)"/>
        <line x1="0" y1="86" x2="258" y2="86" stroke="var(--blue)"/>
      </g>
    </svg>
    <div class="photo" role="img" aria-label="Circular studio portrait of a young woman" style="left:8px;top:14px;width:234px;height:234px;border-radius:50%;border:6px solid var(--magenta);background:radial-gradient(circle at 50% 45%,#e6c7ae 0%,#c79b70 40%,#8d6a48 75%,#e9e6e3 100%)"></div>
    <p class="inside-claim">Tarno Plexa K52 Digital press printer<br>1st one in State of Tasmania</p>
    <p class="printers">2 x Calvor 4400 large format printers</p>
    <p class="printers-note">Will print business cards, brochures, books, postcards, etc more info available on Tarno Plexa website.</p>
    <p class="photo-services"><em>Photography:</em> Studio, Art reproduction, Wedding, Portrait,Commercial, etc.<br>Gallery &amp; studio for hire</p>
    <svg class="stripes" width="258" height="548" viewBox="0 0 258 548" aria-hidden="true">
      <g stroke-width="6">
        <line x1="0" y1="467" x2="76" y2="467" stroke="var(--magenta)"/><line x1="182" y1="467" x2="258" y2="467" stroke="var(--magenta)"/>
        <line x1="0" y1="484" x2="54" y2="484" stroke="var(--cyan)"/><line x1="204" y1="484" x2="258" y2="484" stroke="var(--cyan)"/>
        <line x1="0" y1="501" x2="34" y2="501" stroke="var(--orange)"/><line x1="224" y1="501" x2="258" y2="501" stroke="var(--orange)"/>
        <line x1="0" y1="518" x2="70" y2="518" stroke="var(--green)"/><line x1="188" y1="518" x2="258" y2="518" stroke="var(--green)"/>
        <line x1="0" y1="535" x2="74" y2="535" stroke="var(--blue)"/><line x1="184" y1="535" x2="258" y2="535" stroke="var(--blue)"/>
      </g>
    </svg>
    <ul class="services services--centred">
      <li>Picture Framer</li><li>Fine Art Printing</li><li>Digital Press Printing</li><li>Photographer</li><li>Gallery Studio</li>
    </ul>
  </div>

  <div class="panel panel--white" aria-label="Market panel">
    <div class="photo" role="img" aria-label="Photograph of a busy outdoor market with stalls and crowds" style="left:17px;top:12px;width:241px;height:90px;background:linear-gradient(180deg,#b9c8d6 0%,#9aa7a0 35%,#5d6f62 65%,#4a4a52 100%)"></div>
    <h3 class="market-title">Harbourside Market</h3>
    <div class="market-copy">
      <p>Wendle Quay Press has a stall at Harbourside Market, Wendle every Saturday. The stall is situated between Parliament House and the Law courts.</p>
      <p>On display at Harbourside, are images from Photographers:</p>
      <p class="names">Ned Arlow<br>Tom Brayley<br>Lou Fennick</p>
      <p>The Harbourside gallery shows all images that are available for sale at the market stall.</p>
    </div>
    <svg class="photo" width="258" height="548" viewBox="0 0 258 548" role="img" aria-label="Photograph of a woman reading, seated in a wicker chair" style="left:0;top:0">
      <defs><linearGradient id="roomTone" x1="0" y1="0" x2="1" y2="1"><stop offset="0" stop-color="#c9c6c0"/><stop offset=".5" stop-color="#8f8a82"/><stop offset="1" stop-color="#4e4a46"/></linearGradient></defs>
      <path d="M258 300C150 300 40 380 18 548H258Z" fill="url(#roomTone)"/>
      <path d="M258 300C150 300 40 380 18 548" fill="none" stroke="var(--magenta)" stroke-width="7"/>
    </svg>
  </div>

  <div class="panel" aria-label="Profile panel">
    <div class="photo" role="img" aria-label="Graffiti covered laneway photograph" style="inset:0;background:linear-gradient(170deg,#8a7a8a 0%,#6f6570 35%,#5b6b5c 65%,#4a4a4a 100%)"></div>
    <div class="photo" role="img" aria-label="Circular portrait of the photographer" style="left:20px;top:137px;width:106px;height:106px;border-radius:50%;border:6px solid var(--green);background:radial-gradient(circle at 50% 45%,#e2b99c 0%,#b88a6c 45%,#2d2b2e 80%)"></div>
    <div class="logo-disc" style="left:131px;top:184px;width:82px;height:82px">
      <span class="logo-name" style="font-size:12px">Wendle<br>Quay</span>
    </div>
    <div class="profile-box">
      <h2>Ned Arlow</h2>
      <div class="where">@ Harbourside Market</div>
      <p>Wendle Quay Press has a stall at Harbourside Market, Wendle. The stall is situated between Parliament House and the Law Courts.</p>
      <p>On display are images from Photographers:</p>
      <p class="names">Ned Arlow<br>Tom Brayley<br>Lou Fennick</p>
      <p>The gallery shows all images that are available for sale at the market stall</p>
      <div class="web">www.wendlequaypress.com</div>
    </div>
  </div>
</section>

</body>
</html>
```